Design for Agenda app (online tool) (#102244)

Url of the app: http://notes.bluefernlab.dk

It currently has 3 main parts:
- Front: http://fernhost.dk/screencast/2015-12-01_12-53-36.png
- Dashboard: http://fernhost.dk/screencast/2015-12-01_12-54-16.png
- Meeting page: http://fernhost.dk/screencast/2015-12-01_12-54-53.png

The idea of the app is to have virtual meetings with other people, to take notes/minutes online and to share what is written.

Unregistered users can see only the front.

Registered users can see front, their own dashboard and the meetings which they created or to which they were invited.

The meeting itself has two roles - minute taker an attendee. The attendee can edit only the agenda so he should have different view for the other parts of the meeting compared to the minute taker who can edit everything.

In this doc it is described what are the elements per page which we want to have
https://files.example-docs.net/d/7qXk2LmPz9RtYv4NcBw8HsJd3FgA6eUo1KtQ5WnZ0yE/edit?usp=sharing

As you can see, there is some inconsistency between the front page and the rest of the app. We would like to make it look professional and consistent on all places.

Goal: Get new responsive design where all main parts(front page, dashboard page, meeting page and profile page) will be consistent with each other.

The design should be clean, simple and with very friendly UX.
Updates

Industry/Entity Type

Online

Number of Pages Required

3 page

Font styles to use
Sans Serif

Requirements
Must have
• - Clean and simple
• - Very friendly UX

```html
<!DOCTYPE html>
<html lang="en">
<head>
<meta charset="utf-8">
<title>Bluefern Notes — Log in</title>
<link rel="stylesheet" href="https://fonts.googleapis.com/css2?family=Source+Sans+3:wght@300;400;600&display=swap">
<style>
  :root {
    --bg-dark: #28323d;
    --bg-mid: #2e3945;
    --bg-soft: #35414d;
    --text-light: #e6e9ec;
    --text-white: #ffffff;
    --placeholder: #5c6a78;
    --rule: #8a949e;
    --accent-green: #6cbf6a;
    --accent-amber: #f2a93b;
    --button-text: #3a3226;
  }
  * { box-sizing: border-box; margin: 0; padding: 0; }
  html, body {
    width: 1200px; height: 675px; overflow: hidden;
    font-family: "Source Sans 3", "Source Sans Pro", sans-serif;
    background: var(--bg-dark);
  }
  .login-screen {
    position: relative; width: 1200px; height: 675px; overflow: hidden;
  }
  .backdrop {
    position: absolute; inset: 0;
    background:
      radial-gradient(ellipse at 20% 40%, var(--bg-soft) 0%, transparent 45%),
      radial-gradient(ellipse at 65% 60%, var(--bg-soft) 0%, transparent 50%),
      linear-gradient(180deg, var(--bg-mid) 0%, var(--bg-dark) 100%);
  }
  .site-header {
    position: absolute; top: 0; left: 0; right: 0; height: 156px;
  }
  .brand {
    position: absolute; left: 64px; top: 60px;
    display: flex; align-items: center; gap: 10px;
    color: var(--text-light); font-weight: 300; font-size: 20px;
  }
  .brand-mark { width: 34px; height: 34px; display: block; }
  .signup-prompt {
    position: absolute; right: 77px; top: 66px;
    font-size: 16px; color: var(--text-white); font-weight: 400;
  }
  .signup-prompt a {
    color: var(--accent-green); text-decoration: none; margin-left: 14px;
  }
  .login-form {
    position: absolute; left: 291px; top: 225px; width: 618px;
    text-align: center;
  }
  .login-title {
    font-size: 28px; font-weight: 300; color: var(--text-light);
    letter-spacing: 0.5px; line-height: 40px;
  }
  .login-subtitle {
    margin-top: 15px; font-size: 19px; font-weight: 300;
    color: var(--text-light); line-height: 28px;
  }
  .field {
    display: block; width: 100%; height: 40px;
    border: 0; border-bottom: 1px solid var(--rule);
    background: transparent; color: var(--text-light);
    font: 300 19px "Source Sans 3", "Source Sans Pro", sans-serif;
    padding: 0 12px; outline: none;
  }
  .field::placeholder { color: var(--placeholder); }
  .field-email { margin-top: 13px; }
  .field-password { margin-top: 22px; }
  .login-button {
    display: block; margin: 29px auto 0; width: 97px; height: 30px;
    border: 0; border-radius: 4px; background: var(--accent-amber);
    color: var(--button-text); font: 600 13px "Source Sans 3", "Source Sans Pro", sans-serif;
    letter-spacing: 0.3px;
  }
  .forgot-link {
    display: inline-block; margin-top: 9px; font-size: 14.5px; font-weight: 400;
    color: var(--accent-green); text-decoration: none;
  }
</style>
</head>
<body>
  <main class="login-screen">
    <div class="backdrop" role="img" aria-label="Dimmed photo of a desk with a plant, notebook and pen"></div>

    <header class="site-header">
      <div class="brand">
        <svg class="brand-mark" viewBox="0 0 34 34" aria-hidden="true"><circle cx="17" cy="17" r="16" fill="#4a7fb5"/></svg>
        <span>Bluefern Notes</span>
      </div>
      <div class="signup-prompt">New to Bluefern Notes?<a href="#">SIGN UP</a></div>
    </header>

    <form class="login-form">
      <h1 class="login-title">LOG IN</h1>
      <p class="login-subtitle">Log in to your Bluefern Notes</p>
      <input class="field field-email" type="email" placeholder="Your email">
      <input class="field field-password" type="password" placeholder="Password">
      <button class="login-button" type="button">LOG IN</button>
      <a class="forgot-link" href="#">Forgot password?</a>
    </form>
  </main>
</body>
</html>
```